Intuitive, look stunning website design for the street-level digital media platform that connects audiences with dynamic media on taxis and rideshare vehicles on BACK AND SIDE WINDOWS OF THE VEHICLE. SO FOOT TRAFFIC AND ALL OTHER TRAFFIC CAN SEE DISPLAY ON MOVING VEHICLE (in the future high glass building glass concept)
There should be 7 tabs VORTELANE as home button, advertisers, partners, drivers, about us, news and contact.

Target Market(s)

The company works with taxi companies and rideshare drivers to install its proprietary advertising displays in their vehicles. These proprietary screens deliver dynamic content based on location-based, WiFi-enabled triggers.

Vortelane provides an additional revenue stream to maximize drive time and empowers brands to efficiently engage consumers across our nation's busiest cities, including San Francisco, Los Angeles, New York City, Dallas, Austin, Chicago and Miami.

Industry/Entity Type

Digital Marketing

Coding

Coded - Design and coding required

Number of Pages Required

5+ page

Font styles to use
Sans Serif

Requirements
Must have
• Use beautiful graphics and easy to read fonts.
Make sure graphics are compressed and optimized for fast loading.
Design should be consistent on brand throughout the website design.
Design an intuitive navigation system which allows users to get to the pages they need quickly.
Create pages that are standard for all business from small to big such; home, about us, product/services , sitemap ( seo purposes) contact us etc..
icons links for snapchat, instagram, client login, facbook
Nice to have
• Out of box concept
Should not have
• ITS NOT AN LCD BOX PLACED OVER THE CAR

```html
<!DOCTYPE html>
<html lang="en">
<head>
<meta charset="utf-8">
<title>Vortelane – Street-Level Digital Media Platform</title>
<link rel="stylesheet" href="https://fonts.googleapis.com/css2?family=Lato:wght@300;400;700;900&display=swap">
<style>
:root{
  --blue:#2b93cf;
  --blue-dark:#1f6fa8;
  --navy:#1b3f66;
  --ink:#141414;
  --text:#3a3a3a;
  --muted:#8a8a8a;
  --soft:#f3f4f6;
  --line:#d9d9d9;
  --footer:#1f1f1f;
  --footer-text:#e8e8e8;
  --white:#ffffff;
}
*{box-sizing:border-box;margin:0;padding:0}
html,body{width:1200px;height:4092px;overflow:hidden}
body{font-family:'Lato',sans-serif;color:var(--text);background:var(--white);position:relative}
.abs{position:absolute}
a{color:inherit;text-decoration:none}

/* header */
.topline{left:0;top:0;width:600px;height:4px;background:var(--blue-dark)}
.brand{left:111px;top:10px;display:flex;flex-direction:column;align-items:center;width:110px}
.brand-mark{width:46px;height:46px;border-radius:50%;border:3px solid var(--blue-dark)}
.brand-name{font-weight:700;font-size:14px;letter-spacing:2px;color:var(--ink);margin-top:6px}
.social-top{top:20px;left:769px;display:flex;gap:12px}
.social-circle{width:42px;height:42px;border-radius:50%;border:1.5px solid #cfcfcf;display:flex;align-items:center;justify-content:center}
.login{left:927px;top:16px;width:162px;height:48px;border-radius:24px;background:var(--blue);color:var(--white);font-weight:700;font-size:15px;display:flex;align-items:center;justify-content:center;gap:6px}
.nav{top:82px;left:344px;display:flex;align-items:center;gap:32px;font-size:15.5px;font-weight:700;color:var(--ink)}
.nav .active{color:var(--blue)}

/* hero */
.hero{left:0;top:116px;width:1200px;height:532px;background:linear-gradient(100deg,#1d3f6a 0%,#2a5d8c 35%,#8a6a2a 60%,#d8a11d 80%,#c98a2a 100%)}
.hero-title{left:111px;top:160px;font-weight:900;font-size:60px;line-height:74px;color:var(--white)}
.hero-sub{left:111px;top:405px;font-size:23px;line-height:36px;color:var(--white)}
.btn-white{background:var(--white);color:var(--ink);font-weight:700;border-radius:34px;display:flex;align-items:center;justify-content:center;letter-spacing:.5px}
.hero-btn{left:111px;top:515px;width:216px;height:64px;font-size:18px}
.dots{left:584px;top:589px;display:flex;gap:6px}
.dot{width:13px;height:13px;border-radius:50%;border:2px solid var(--white)}
.dot.on{background:var(--white)}

/* section titles */
.sec-title{left:0;width:1200px;text-align:center;font-weight:900;font-size:40px;color:var(--ink)}

/* badge strip */
.strip{left:108px;display:flex;gap:16px}
.badge{width:184px;height:98px;border:1.5px solid #cfcfcf;background:var(--white);display:flex;align-items:center;justify-content:center}
.badge span{width:130px;height:34px;border-radius:6px;background:#c4c4c4}
.badge span.dark{background:#1d2a4a}
.arrow{width:24px;height:40px}

/* welcome */
.welcome-title{left:111px;top:955px;font-weight:900;font-size:40px;line-height:48px;color:var(--ink)}
.body-copy{font-size:16px;line-height:29px;color:#555}
.welcome-copy{left:111px;top:1064px;width:440px}
.btn-blue{background:var(--blue);color:var(--white);font-weight:700;font-size:16px;border-radius:26px;display:flex;align-items:center;justify-content:center}
.welcome-btn{left:111px;top:1233px;width:162px;height:51px}
.video{left:599px;top:965px;width:490px;height:288px;background:linear-gradient(135deg,#5a5a5a 0%,#c8a234 40%,#e0b23a 60%,#7a6a4a 100%);box-shadow:0 2px 6px rgba(0,0,0,.35)}
.play{left:815px;top:1081px;width:58px;height:58px}

/* why choose */
.why{left:0;top:1343px;width:1200px;height:647px;background:var(--soft)}
.feature{width:330px;text-align:center}
.feature svg{display:block;margin:0 auto}
.feature h3{font-weight:400;font-size:22px;color:var(--ink);margin-top:18px}
.feature p{font-size:15.5px;line-height:28px;color:var(--muted);margin-top:12px}

/* outdoor */
.outdoor-img{left:143px;top:2015px;width:398px;height:398px;border-radius:50%;border:14px solid var(--blue-dark);background:radial-gradient(circle at 40% 35%,#c94a7a 0%,#3a6ab0 45%,#e0a020 80%,#d98a10 100%)}
.outdoor-title{left:656px;top:2036px;font-weight:900;font-size:40px;line-height:46px;color:var(--ink)}
.outdoor-copy{left:655px;top:2146px;width:440px}
.outdoor-btn{left:655px;top:2315px;width:161px;height:51px}

/* cta */
.cta{left:0;top:2447px;width:1200px;height:375px;background:linear-gradient(90deg,#2e8fc4 0%,#4aa6d6 50%,#2f86bb 100%)}
.cta-title{left:0;top:2495px;width:1200px;text-align:center;font-weight:900;font-size:40px;line-height:52px;color:var(--white)}
.cta-copy{left:0;top:2616px;width:1200px;text-align:center;font-size:16px;line-height:29px;color:var(--white)}
.cta-btn{left:486px;top:2698px;width:228px;height:67px;font-size:20px}

/* news */
.card{top:2956px;width:303px;height:432px;background:var(--white);box-shadow:0 2px 8px rgba(0,0,0,.14)}
.card-img{width:303px;height:202px}
.card-body{padding:22px 24px}
.card h4{font-weight:400;font-size:18px;line-height:29px;color:var(--ink)}
.meta{font-size:14px;color:var(--muted);margin-top:14px;display:flex;align-items:center;gap:8px}
.meta .ico{color:var(--blue)}
.card p{font-size:14px;line-height:27px;color:var(--muted);margin-top:10px}
.more{font-size:14.5px;font-weight:700;color:var(--blue);margin-top:12px;display:block}

/* partners */
.partners{left:0;top:3459px;width:1200px;height:278px;background:var(--soft)}

/* footer */
.footer{left:0;top:3737px;width:1200px;height:355px;background:var(--footer)}
.f-col{color:var(--footer-text)}
.f-head{font-weight:700;font-size:20px;color:var(--white)}
.f-links{list-style:none;font-size:14.5px;line-height:25.8px;margin-top:18px;color:var(--footer-text)}
.f-text{font-size:14.5px;line-height:25.8px;margin-top:18px;color:var(--footer-text)}
.news-input{left:607px;top:3890px;width:268px;height:44px;background:var(--white);color:#9a9a9a;font-size:14px;display:flex;align-items:center;padding-left:20px;gap:8px}
.news-btn{left:875px;top:3890px;width:93px;height:44px;background:var(--blue);color:var(--white);font-weight:700;font-size:13.5px;display:flex;align-items:center;justify-content:center}
.f-rule{left:106px;top:4023px;width:994px;height:1px;background:#444}
.copyright{left:106px;top:4043px;font-size:14px;color:var(--footer-text)}
.f-social{left:945px;top:4030px;display:flex;gap:10px}
.f-social .social-circle{border-color:#aaa;width:46px;height:46px}
</style>
</head>
<body>

<!-- Header -->
<div class="abs topline"></div>
<div class="abs brand"><div class="brand-mark"></div><div class="brand-name">VORTELANE</div></div>
<div class="abs social-top" aria-label="Social links">
  <a class="social-circle" aria-label="Social network"><svg width="16" height="16" viewBox="0 0 16 16"><circle cx="4" cy="8" r="2.3" fill="var(--blue)"/><circle cx="12" cy="3.5" r="2.3" fill="var(--blue)"/><circle cx="12" cy="12.5" r="2.3" fill="var(--blue)"/><path d="M4 8l8-4.5M4 8l8 4.5" stroke="var(--blue)" stroke-width="1.4"/></svg></a>
  <a class="social-circle" aria-label="Social network"><svg width="16" height="16" viewBox="0 0 16 16"><circle cx="4" cy="8" r="2.3" fill="var(--blue)"/><circle cx="12" cy="3.5" r="2.3" fill="var(--blue)"/><circle cx="12" cy="12.5" r="2.3" fill="var(--blue)"/><path d="M4 8l8-4.5M4 8l8 4.5" stroke="var(--blue)" stroke-width="1.4"/></svg></a>
  <a class="social-circle" aria-label="Social network"><svg width="16" height="16" viewBox="0 0 16 16"><circle cx="4" cy="8" r="2.3" fill="var(--blue)"/><circle cx="12" cy="3.5" r="2.3" fill="var(--blue)"/><circle cx="12" cy="12.5" r="2.3" fill="var(--blue)"/><path d="M4 8l8-4.5M4 8l8 4.5" stroke="var(--blue)" stroke-width="1.4"/></svg></a>
</div>
<a class="abs login"><svg width="14" height="14" viewBox="0 0 14 14"><circle cx="7" cy="4" r="3" fill="#fff"/><path d="M1 14c0-4 3-6 6-6s6 2 6 6z" fill="#fff"/></svg>CLIENT LOGIN</a>
<nav class="abs nav">
  <a class="active">HOME</a><a>ADVERTISERS</a><a>PARTNERS</a><a>DRIVERS</a><a>ABOUT US</a><a>NEWS</a><a>CONTACT</a>
  <svg width="16" height="16" viewBox="0 0 16 16"><circle cx="6.5" cy="6.5" r="4.5" fill="none" stroke="#141414" stroke-width="2"/><path d="M10 10l4 4" stroke="#141414" stroke-width="2.4"/></svg>
</nav>

<!-- Hero -->
<div class="abs hero" role="img" aria-label="Photo of a yellow taxi on a city street with a woman reading her phone"></div>
<h1 class="abs hero-title">STREET-LEVEL<br>DIGITAL MEDIA<br>PLATFORM</h1>
<p class="abs hero-sub">Connects audiences with dynamic media<br>on taxis and rideshare vehicles.</p>
<a class="abs btn-white hero-btn">GET MORE INFO</a>
<div class="abs dots"><span class="dot on"></span><span class="dot"></span><span class="dot"></span></div>

<!-- Advertisers -->
<h2 class="abs sec-title" style="top:705px">ADVERTISERS</h2>
<svg class="abs arrow" style="left:46px;top:816px" viewBox="0 0 24 40"><path d="M18 6L6 20l12 14" fill="none" stroke="#666" stroke-width="3"/></svg>
<div class="abs strip" style="top:787px">
  <div class="badge"><span></span></div><div class="badge"><span></span></div><div class="badge"><span class="dark"></span></div><div class="badge"><span></span></div><div class="badge"><span></span></div>
</div>
<svg class="abs arrow" style="left:1130px;top:816px" viewBox="0 0 24 40"><path d="M6 6l12 14L6 34" fill="none" stroke="#666" stroke-width="3"/></svg>

<!-- Welcome -->
<h2 class="abs welcome-title">WELCOME<br>TO VORTELANE</h2>
<p class="abs body-copy welcome-copy">Lorem ipsum dolor sit amet, consectetur adipiscing elit, sed do eiusmod tempor incididunt ut labore et dolore magnaliq ua. Ut enim ad minim veniam, quis nostrud exercitation ulla mco laboris nisi ut aliquip ex ea commodo consequat. Duisu te irure dolor in reprehenderit in volu.</p>
<a class="abs btn-blue welcome-btn">READ MORE</a>
<div class="abs video" role="img" aria-label="Video still of a yellow taxi with passengers"></div>
<svg class="abs play" viewBox="0 0 58 58"><circle cx="29" cy="29" r="29" fill="#111"/><path d="M23 18l16 11-16 11z" fill="#fff"/></svg>

<!-- Why choose us -->
<div class="abs why"></div>
<h2 class="abs sec-title" style="top:1398px">WHY CHOOSE US</h2>

<div class="abs feature" style="left:91px;top:1475px">
  <svg width="110" height="110" viewBox="0 0 110 110"><circle cx="55" cy="55" r="52" fill="none" stroke="var(--navy)" stroke-width="3" stroke-dasharray="150 13"/><rect x="36" y="45" width="38" height="22" rx="2" fill="none" stroke="var(--blue)" stroke-width="3"/><circle cx="55" cy="56" r="5" fill="var(--blue)"/></svg>
  <h3>Economic Cost</h3><p>Nemo enim ipsam voluptatem quia volu<br>ptas sit aspernatur aut odit aut fu</p>
</div>
<div class="abs feature" style="left:434px;top:1475px">
  <svg width="110" height="110" viewBox="0 0 110 110"><circle cx="55" cy="55" r="52" fill="none" stroke="var(--navy)" stroke-width="3" stroke-dasharray="150 13"/><circle cx="55" cy="55" r="13" fill="none" stroke="var(--blue)" stroke-width="3"/><path d="M55 48v8h5" fill="none" stroke="var(--blue)" stroke-width="2.5"/></svg>
  <h3>Perfectly Timed</h3><p>Nemo enim ipsam voluptatem quia volu<br>ptas sit aspernatur aut odit aut fu</p>
</div>
<div class="abs feature" style="left:779px;top:1475px">
  <svg width="110" height="110" viewBox="0 0 110 110"><circle cx="55" cy="55" r="52" fill="none" stroke="var(--navy)" stroke-width="3" stroke-dasharray="150 13"/><ellipse cx="55" cy="44" rx="15" ry="5" fill="var(--blue)"/><rect x="40" y="48" width="30" height="6" rx="3" fill="var(--blue)"/><rect x="40" y="56" width="30" height="6" rx="3" fill="var(--blue)"/><rect x="40" y="64" width="30" height="6" rx="3" fill="var(--blue)"/></svg>
  <h3>Reach &amp; Data</h3><p>Nemo enim ipsam voluptatem quia volu<br>ptas sit aspernatur aut odit aut fu</p>
</div>
<div class="abs feature" style="left:91px;top:1716px">
  <svg width="110" height="110" viewBox="0 0 110 110"><circle cx="55" cy="55" r="52" fill="none" stroke="var(--navy)" stroke-width="3" stroke-dasharray="150 13"/><circle cx="50" cy="58" r="8" fill="none" stroke="var(--blue)" stroke-width="5" stroke-dasharray="4 2.3"/><circle cx="64" cy="46" r="5" fill="none" stroke="var(--blue)" stroke-width="4" stroke-dasharray="3 1.8"/></svg>
  <h3>Maintenance</h3><p>Nemo enim ipsam voluptatem quia volu<br>ptas sit aspernatur aut odit aut fu</p>
</div>
<div class="abs feature" style="left:434px;top:1716px">
  <svg width="110" height="110" viewBox="0 0 110 110"><circle cx="55" cy="55" r="52" fill="none" stroke="var(--navy)" stroke-width="3" stroke-dasharray="150 13"/><path d="M37 55c10-12 26-12 36 0-10 12-26 12-36 0z" fill="none" stroke="var(--blue)" stroke-width="3"/><circle cx="55" cy="55" r="5" fill="var(--blue)"/></svg>
  <h3>Appealing to the Eyes</h3><p>Nemo enim ipsam voluptatem quia volu<br>ptas sit aspernatur aut odit aut fu</p>
</div>
<div class="abs feature" style="left:779px;top:1716px">
  <svg width="110" height="110" viewBox="0 0 110 110"><circle cx="55" cy="55" r="52" fill="none" stroke="var(--navy)" stroke-width="3" stroke-dasharray="150 13"/><path d="M38 54l32-14-8 32-8-10z M54 62l16-22" fill="none" stroke="var(--blue)" stroke-width="3" stroke-linejoin="round"/></svg>
  <h3>Extensive Reach</h3><p>Nemo enim ipsam voluptatem quia volu<br>ptas sit aspernatur aut odit aut fu</p>
</div>

<!-- Digital outdoor advertising -->
<div class="abs outdoor-img" role="img" aria-label="Round photo of a taxi roof display in a bright city square"></div>
<h2 class="abs outdoor-title">DIGITAL OUTDOOR<br>ADVERTISING</h2>
<p class="abs body-copy outdoor-copy">Lorem ipsum dolor sit amet, consectetur adipiscing elit, sed do eiusmod tempor incididunt ut labore et dolore magnaliq ua. Ut enim ad minim veniam, quis nostrud exercitation ulla mco laboris nisi ut aliquip ex ea commodo consequat. Duisu te irure dolor in reprehenderit in volu.</p>
<a class="abs btn-blue outdoor-btn">READ MORE</a>

<!-- CTA -->
<div class="abs cta" role="img" aria-label="Blue-tinted photo of taxis in traffic"></div>
<h2 class="abs cta-title">LOOKING FOR<br>AFFORDABLE ADVERTISEMENT SPACES?</h2>
<p class="abs cta-copy">Ut enim ad minima veniam, quis nostrum exercitationem ullam corporis suscipit labo<br>riosam, nisi ut aliquid ex ea commodi consequatu</p>
<a class="abs btn-white cta-btn">GET A QUOTE</a>

<!-- News -->
<h2 class="abs sec-title" style="top:2876px">IN THE NEWS</h2>
<article class="abs card" style="left:111px">
  <div class="card-img" role="img" aria-label="Photo of yellow taxis in a busy square with billboards" style="background:linear-gradient(180deg,#3c6db0 0%,#c2503c 55%,#e0a824 100%)"></div>
  <div class="card-body"><h4>Nam libero tempore, cum solu<br>ta nobis est eligendi</h4>
  <div class="meta"><span><span class="ico">&#9633;</span> May 23, 2020</span><span>|</span><span><span class="ico">&#9679;</span> John</span></div>
  <p>At vero eos et accusamus et iusto odio digni ssi mos ducimus qui bla..</p><a class="more">READ MORE</a></div>
</article>
<article class="abs card" style="left:440px">
  <div class="card-img" role="img" aria-label="Photo of night traffic light trails in a city" style="background:linear-gradient(180deg,#1f2a4a 0%,#3b4f8a 50%,#d8d8e8 100%)"></div>
  <div class="card-body"><h4>Nam libero tempore, cum solu<br>ta nobis est eligendi</h4>
  <div class="meta"><span><span class="ico">&#9633;</span> May 23, 2020</span><span>|</span><span><span class="ico">&#9679;</span> John</span></div>
  <p>At vero eos et accusamus et iusto odio digni ssi mos ducimus qui bla..</p><a class="more">READ MORE</a></div>
</article>
<article class="abs card" style="left:767px">
  <div class="card-img" role="img" aria-label="Photo of yellow taxis on a grey city avenue" style="background:linear-gradient(180deg,#8a8a8a 0%,#5a5a5a 55%,#c89a20 100%)"></div>
  <div class="card-body"><h4>Nam libero tempore, cum solu<br>ta nobis est eligendi</h4>
  <div class="meta"><span><span class="ico">&#9633;</span> May 23, 2020</span><span>|</span><span><span class="ico">&#9679;</span> John</span></div>
  <p>At vero eos et accusamus et iusto odio digni ssi mos ducimus qui bla..</p><a class="more">READ MORE</a></div>
</article>

<!-- Partners -->
<div class="abs partners"></div>
<h2 class="abs sec-title" style="top:3500px">PARTNERS</h2>
<svg class="abs arrow" style="left:46px;top:3612px" viewBox="0 0 24 40"><path d="M18 6L6 20l12 14" fill="none" stroke="#666" stroke-width="3"/></svg>
<div class="abs strip" style="top:3583px">
  <div class="badge"><span></span></div><div class="badge"><span></span></div><div class="badge"><span class="dark"></span></div><div class="badge"><span></span></div><div class="badge"><span></span></div>
</div>
<svg class="abs arrow" style="left:1130px;top:3612px" viewBox="0 0 24 40"><path d="M6 6l12 14L6 34" fill="none" stroke="#666" stroke-width="3"/></svg>

<!-- Footer -->
<footer class="abs footer"></footer>
<div class="abs f-col" style="left:111px;top:3779px">
  <div class="f-head">Company</div>
  <ul class="f-links"><li>Home</li><li>Advertisers</li><li>Partners</li><li>Drivers</li><li>About us</li><li>News</li><li>Contact</li></ul>
</div>
<div class="abs f-col" style="left:351px;top:3779px">
  <div class="f-head">Quick Links</div>
  <ul class="f-links"><li>Help</li><li>FAQ</li><li>Terms &amp; conditions</li><li>Return Policy</li><li>Customer Support</li></ul>
</div>
<div class="abs f-col" style="left:605px;top:3779px;width:380px">
  <div class="f-head">Newsletter Subscription</div>
  <p class="f-text">Register your Email Address to get information<br>about us</p>
</div>
<div class="abs news-input"><svg width="14" height="11" viewBox="0 0 14 11"><rect x="0.5" y="0.5" width="13" height="10" fill="none" stroke="#9a9a9a"/><path d="M1 1l6 5 6-5" fill="none" stroke="#9a9a9a"/></svg>Email Address</div>
<a class="abs news-btn">SUBSCRIBE</a>
<div class="abs f-rule"></div>
<p class="abs copyright">Copyrights © 2020, Vortelane.</p>
<div class="abs f-social" aria-label="Social links">
  <a class="social-circle" aria-label="Social network"><svg width="16" height="16" viewBox="0 0 16 16"><circle cx="4" cy="8" r="2.3" fill="#fff"/><circle cx="12" cy="3.5" r="2.3" fill="#fff"/><circle cx="12" cy="12.5" r="2.3" fill="#fff"/><path d="M4 8l8-4.5M4 8l8 4.5" stroke="#fff" stroke-width="1.4"/></svg></a>
  <a class="social-circle" aria-label="Social network"><svg width="16" height="16" viewBox="0 0 16 16"><circle cx="4" cy="8" r="2.3" fill="#fff"/><circle cx="12" cy="3.5" r="2.3" fill="#fff"/><circle cx="12" cy="12.5" r="2.3" fill="#fff"/><path d="M4 8l8-4.5M4 8l8 4.5" stroke="#fff" stroke-width="1.4"/></svg></a>
  <a class="social-circle" aria-label="Social network"><svg width="16" height="16" viewBox="0 0 16 16"><circle cx="4" cy="8" r="2.3" fill="#fff"/><circle cx="12" cy="3.5" r="2.3" fill="#fff"/><circle cx="12" cy="12.5" r="2.3" fill="#fff"/><path d="M4 8l8-4.5M4 8l8 4.5" stroke="#fff" stroke-width="1.4"/></svg></a>
</div>

</body>
</html>
```